Webdesign für einen Hersteller von hochpräzisen Durchflussmessern und Drucksensoren
Zielgruppe
Wir sind die KTV GmbH & Co. KG, ein deutscher Hersteller von hochpräzisen Durchflussmessern und Drucksensoren für industrielle Anwendungen. Unsere Produkte werden weltweit in Prüfständen, Automotive-Testing, Maschinenbau, Energie- und Prozessindustrie eingesetzt.
Unsere Zielgruppe sind technische Entscheider, Ingenieure, Entwicklungsleiter und Einkäufer in B2B-Unternehmen. Die Website dient als Produkt- und Markenpräsentation, Lead-Generierung sowie als Vertrauensbasis vor Kontaktaufnahme oder Angebotsanfrage.
Wichtig ist ein hochwertiger, technologischer, international verständlicher Auftritt, der Kompetenz, Präzision und Innovationskraft vermittelt.
Aufgabenstellung
Es existiert bereits ein Logo und Corporate Design, das beibehalten werden soll. Die neue Gestaltung des bestehenden Wordpress-Auftritts soll dieses modernisieren und konsistenter anwenden.
Designstil:
• Modern, clean, technisch, hochwertig
• Viel Weißraum, klare Typografie
• Präzise Linien, dezente technische Grafikelemente
Farben:
• Bestehende Markenfarben aus dem Logo beibehalten
• Hauptfarbe: Blau / Dunkelblau
• Ergänzend Grau- und Weißtöne
• Akzentfarben #d15c04 sparsam einsetzen
Bildsprache:
• Hochwertige Produktfotos
• Industrie- und Anwendungsszenen
• Detailaufnahmen von Sensoren / Technik
• Optional abstrakte technische Visuals oder Liniengrafiken
UX-Anforderungen:
• Klare Navigation für Produktbereiche
• Schneller Zugang zu Produktdetails
• Call-to-Action für Kontakt / Anfrage
• International verständliches Layout (englische Seite folgt später)
Technische Hinweise:
• Die Seite wird später in WordPress umgesetzt
• Responsive Design für Desktop / Tablet / Mobile
• SEO-freundliche Struktur
Design-Tool Präferenz:
• Figma bevorzugt

```html
<!DOCTYPE html>
<html lang="de">
<head>
<meta charset="utf-8">
<title>KTV Sensorik – Präzise Messtechnik</title>
<link href="https://fonts.googleapis.com/css2?family=Inter:wght@400;500;600;700&family=Plus+Jakarta+Sans:wght@600;700;800&display=swap" rel="stylesheet">
<style>
:root{
  --navy:#0a2f66;
  --navy-deep:#082654;
  --orange:#d15c04;
  --ink:#14213a;
  --muted:#5f6878;
  --line:#e3e6ec;
  --paper:#ffffff;
  --mist:#f4f5f7;
}
*{box-sizing:border-box;margin:0;padding:0}
html,body{width:1200px;height:2645px;overflow:hidden}
body{font-family:"Inter",sans-serif;color:var(--ink);background:var(--paper);font-size:13px}
.wrap{width:1000px;margin:0 auto}
h1,h2,h3{font-family:"Plus Jakarta Sans",sans-serif}
svg{display:block}

/* nav */
.nav{height:56px;background:#fff;border-bottom:1px solid var(--line)}
.nav .wrap{display:flex;align-items:center;height:100%}
.brand{font-family:"Inter",sans-serif;font-weight:700;font-size:22px;color:var(--navy);display:flex;align-items:center;gap:8px;letter-spacing:-.3px}
.brand-dot{width:12px;height:12px;background:var(--navy);border-radius:2px}
.menu{display:flex;gap:6px;margin-left:282px;align-items:center}
.menu a{font-size:12px;font-weight:500;color:var(--ink);padding:8px 12px;border-radius:4px;text-decoration:none;display:flex;align-items:center;gap:4px}
.menu a.active{background:var(--orange);color:#fff}
.nav-right{margin-left:auto;display:flex;align-items:center;gap:14px}
.shop{font-size:12px;font-weight:500;display:flex;gap:5px;align-items:center}
.btn-contact{background:var(--navy);color:#fff;font-size:12px;font-weight:600;padding:8px 11px;border-radius:4px}

/* hero */
.hero{height:470px;position:relative;overflow:hidden;
  background:linear-gradient(90deg,#0c2f66 0%,#113a72 40%,#1f4b7d 65%,#34506e 100%)}
.hero-visual{position:absolute;inset:0;background:
  radial-gradient(ellipse 260px 220px at 830px 190px,rgba(150,180,200,.35),transparent 70%),
  radial-gradient(ellipse 200px 160px at 1130px 120px,rgba(210,120,60,.25),transparent 70%)}
.hero-fade{position:absolute;left:0;right:0;bottom:0;height:120px;background:linear-gradient(180deg,rgba(255,255,255,0),#fff)}
.hero .wrap{position:relative;padding-top:82px;color:#fff}
.pill{display:inline-flex;align-items:center;gap:6px;font-size:10px;font-weight:500;padding:6px 12px;border:1px solid rgba(255,255,255,.3);background:rgba(255,255,255,.12);border-radius:20px}
.pill i{width:5px;height:5px;background:var(--orange);border-radius:50%}
.hero h1{font-size:44px;line-height:1.02;font-weight:800;margin-top:18px;letter-spacing:-.8px}
.hero h1 span{color:var(--orange)}
.hero p{font-size:14px;line-height:1.5;width:410px;margin-top:26px;color:#e3eaf4}
.checks{display:flex;gap:18px;margin-top:14px;font-size:10.5px;color:#dfe6f1}
.checks span{display:flex;align-items:center;gap:5px}
.hero-cta{display:flex;gap:12px;margin-top:28px}
.btn-orange{background:var(--orange);color:#fff;font-size:12px;font-weight:600;padding:0 24px;height:38px;display:inline-flex;align-items:center;gap:12px;border-radius:3px}
.btn-blank{width:162px;height:38px;background:#fff;border-radius:3px}

/* products */
.products{background:var(--mist);padding:30px 0 56px;height:820px}
.eyebrow{font-size:10px;font-weight:600;letter-spacing:.6px;color:var(--orange);text-align:center;text-transform:uppercase}
.section-title{font-size:27px;font-weight:700;text-align:center;color:var(--navy-deep);margin-top:12px}
.section-sub{font-size:12px;color:var(--muted);text-align:center;width:470px;margin:12px auto 0;line-height:1.55}
.cards{display:grid;grid-template-columns:1fr 1fr;gap:24px;margin-top:48px}
.card{background:#fff;border-radius:4px;box-shadow:0 2px 10px rgba(10,30,70,.06);overflow:hidden}
.card-img{height:345px}
.img-flow{background:linear-gradient(135deg,#1d3f78 0%,#6d86a8 45%,#c8ced6 75%,#eef0f3 100%)}
.img-press{background:linear-gradient(135deg,#f3f3f3 0%,#d9d6cf 45%,#b9b2a4 70%,#f2f2f2 100%)}
.card-body{padding:26px 24px 26px}
.card h3{font-size:17px;font-weight:700;color:var(--navy-deep)}
.card p{font-size:11.5px;color:var(--muted);line-height:1.55;margin-top:10px;width:420px}
.tags{display:flex;gap:8px;margin-top:10px}
.tags span{font-size:9px;font-weight:600;background:var(--mist);padding:5px 9px;border-radius:12px;color:var(--ink)}
.btn-navy{margin-top:16px;background:var(--navy);color:#fff;font-size:11px;font-weight:600;padding:8px 13px;border-radius:3px;display:inline-flex;gap:10px;align-items:center}

/* advantages */
.advantages{height:545px;padding-top:66px;background:#fff}
.adv-grid{display:grid;grid-template-columns:repeat(3,1fr);gap:24px;margin-top:48px}
.adv{border:1px solid var(--line);border-radius:4px;padding:20px 18px;height:146px}
.adv-icon{width:32px;height:32px;background:var(--mist);border-radius:4px;display:flex;align-items:center;justify-content:center}
.adv h3{font-family:"Inter",sans-serif;font-size:13px;font-weight:600;margin-top:18px;color:var(--navy-deep)}
.adv p{font-size:10.5px;color:var(--muted);line-height:1.55;margin-top:8px}

/* industries */
.industries{background:var(--navy);height:235px;color:#fff}
.industries .wrap{display:flex;justify-content:space-between;padding-top:44px}
.ind-text{padding-top:42px}
.ind-text h2{font-size:21px;font-weight:700}
.ind-text p{font-size:11.5px;line-height:1.55;color:#c9d4e6;width:350px;margin-top:10px}
.tiles{display:flex;flex-wrap:wrap;justify-content:flex-end;gap:14px;width:560px}
.tile{background:rgba(255,255,255,.1);border-radius:4px;height:64px;padding:0 12px;display:flex;flex-direction:column;align-items:center;justify-content:center;gap:8px;font-size:9px;font-weight:600}

/* cta */
.cta{height:325px;text-align:center;padding-top:84px}
.cta h2{font-size:27px;font-weight:700;color:var(--navy-deep)}
.cta p{font-size:13px;line-height:1.6;color:var(--muted);width:510px;margin:14px auto 0}
.cta-row{display:flex;justify-content:center;gap:14px;margin-top:22px}
.btn-outline{height:38px;border:1px solid var(--line);border-radius:3px;padding:0 24px;display:inline-flex;gap:8px;align-items:center;font-size:12px;font-weight:600}
.cta small{display:block;margin-top:18px;font-size:10.5px;color:var(--muted)}
.cta small b{color:var(--orange)}

/* footer */
.footer{background:var(--navy);color:#fff;height:245px;padding-top:40px}
.foot-grid{display:grid;grid-template-columns:256px 256px 256px 1fr;height:138px}
.footer .brand{color:#fff;font-size:22px}
.footer .brand-dot{background:#fff}
.foot-about{font-size:10.5px;line-height:1.6;color:#d3dbe8;margin-top:14px;width:230px}
.foot-col h4{font-size:12px;font-weight:600}
.foot-col li{list-style:none;font-size:10.5px;color:#d3dbe8;margin-top:8px;display:flex;gap:8px;line-height:1.45}
.foot-bottom{border-top:1px solid rgba(255,255,255,.12);padding-top:18px;display:flex;justify-content:space-between;font-size:10px;color:#b8c4d8}
.foot-bottom nav{display:flex;gap:18px}
</style>
</head>
<body>

<header class="nav">
  <div class="wrap">
    <div class="brand"><span class="brand-dot"></span>KTV Sensorik</div>
    <nav class="menu">
      <a class="active">Startseite</a>
      <a>Produkte <svg width="8" height="8" viewBox="0 0 8 8"><path d="M1 3l3 3 3-3" fill="none" stroke="#14213a" stroke-width="1.2"/></svg></a>
      <a>Ratgeber</a>
    </nav>
    <div class="nav-right">
      <span class="shop"><svg width="13" height="13" viewBox="0 0 16 16" fill="none" stroke="#14213a" stroke-width="1.4"><path d="M1 2h2.5l1.8 8h8l1.5-6H4.3"/><circle cx="6" cy="13.5" r="1"/><circle cx="12" cy="13.5" r="1"/></svg>Shop</span>
      <span class="btn-contact">Kontakt</span>
    </div>
  </div>
</header>

<section class="hero">
  <div class="hero-visual" role="img" aria-label="Industriehalle mit Durchflussmesser und Manometer in unscharfer Tiefe"></div>
  <div class="hero-fade"></div>
  <div class="wrap">
    <span class="pill"><i></i>Made in Germany – Präzision seit 1990</span>
    <h1>Präzise Messtechnik<br>für <span>industrielle<br>Exzellenz</span></h1>
    <p>Hochwertige Durchflussmesser und Drucksensoren für anspruchsvolle Industrieanwendungen. Entwickelt und gefertigt in Deutschland.</p>
    <div class="checks">
      <span><svg width="10" height="10" viewBox="0 0 12 12"><circle cx="6" cy="6" r="5" fill="none" stroke="#d15c04"/><path d="M3.5 6l1.8 1.8L8.5 4.5" fill="none" stroke="#d15c04"/></svg>Höchste Präzision</span>
      <span><svg width="10" height="10" viewBox="0 0 12 12"><circle cx="6" cy="6" r="5" fill="none" stroke="#d15c04"/><path d="M3.5 6l1.8 1.8L8.5 4.5" fill="none" stroke="#d15c04"/></svg>ISO-zertifiziert</span>
      <span><svg width="10" height="10" viewBox="0 0 12 12"><circle cx="6" cy="6" r="5" fill="none" stroke="#d15c04"/><path d="M3.5 6l1.8 1.8L8.5 4.5" fill="none" stroke="#d15c04"/></svg>Individuelle Kalibrierung</span>
    </div>
    <div class="hero-cta">
      <span class="btn-orange">Produkte entdecken <svg width="10" height="10" viewBox="0 0 10 10"><path d="M1 5h8M5.5 1.5L9 5 5.5 8.5" fill="none" stroke="#fff" stroke-width="1.3"/></svg></span>
      <span class="btn-blank"></span>
    </div>
  </div>
</section>

<section class="products">
  <div class="wrap">
    <div class="eyebrow">Unsere Produktbereiche</div>
    <h2 class="section-title">Messtechnik auf höchstem Niveau</h2>
    <p class="section-sub">Zwei Produktbereiche, ein Qualitätsanspruch: Deutsche Ingenieurskunst für Ihre anspruchsvollsten Messaufgaben.</p>
    <div class="cards">
      <article class="card">
        <div class="card-img img-flow" role="img" aria-label="Nahaufnahme eines Durchflussmessers mit digitaler Anzeige"></div>
        <div class="card-body">
          <h3>Durchflussmesser</h3>
          <p>Präzise Durchflussmessung für Flüssigkeiten und Gase. Von kompakten Inline-Sensoren bis hin zu hochpräzisen Laborgeräten.</p>
          <div class="tags"><span>Ultraschall-Technologie</span><span>Volumetrische Messung</span><span>Thermische Messung</span></div>
          <span class="btn-navy">Alle Durchflussmesser ansehen <svg width="9" height="9" viewBox="0 0 10 10"><path d="M1 5h8M5.5 1.5L9 5 5.5 8.5" fill="none" stroke="#fff" stroke-width="1.3"/></svg></span>
        </div>
      </article>
      <article class="card">
        <div class="card-img img-press" role="img" aria-label="Edelstahl-Drucksensor mit Anschlusskabel"></div>
        <div class="card-body">
          <h3>Drucksensoren</h3>
          <p>Hochgenaue Druckmessung für industrielle Prozesse. Robust, langlebig und kalibrierbar.</p>
          <div class="tags"><span>Absolutdruck</span><span>Relativdruck</span><span>Differenzdruck</span></div>
          <span class="btn-navy">Alle Drucksensoren ansehen <svg width="9" height="9" viewBox="0 0 10 10"><path d="M1 5h8M5.5 1.5L9 5 5.5 8.5" fill="none" stroke="#fff" stroke-width="1.3"/></svg></span>
        </div>
      </article>
    </div>
  </div>
</section>

<section class="advantages">
  <div class="wrap">
    <div class="eyebrow">Warum KTV Sensorik</div>
    <h2 class="section-title">Ihre Vorteile auf einen Blick</h2>
    <p class="section-sub">Vertrauen Sie auf über 30 Jahre Erfahrung in der Entwicklung und Fertigung von Präzisionsmesstechnik.</p>
    <div class="adv-grid">
      <div class="adv"><div class="adv-icon"><svg width="14" height="14" viewBox="0 0 16 16" fill="none" stroke="#0a2f66" stroke-width="1.4"><path d="M2 12a6 6 0 1 1 12 0"/><path d="M8 11l3-4"/></svg></div><h3>Höchste Präzision</h3><p>Messgenauigkeit bis ±0,1% für zuverlässige Prozesssteuerung und Qualitätssicherung.</p></div>
      <div class="adv"><div class="adv-icon"><svg width="14" height="14" viewBox="0 0 16 16" fill="none" stroke="#0a2f66" stroke-width="1.4"><circle cx="8" cy="6" r="4"/><path d="M5.5 9.5L5 15l3-1.5 3 1.5-.5-5.5"/></svg></div><h3>Made in Germany</h3><p>Entwicklung und Fertigung in Deutschland nach höchsten Qualitätsstandards.</p></div>
      <div class="adv"><div class="adv-icon"><svg width="14" height="14" viewBox="0 0 16 16" fill="none" stroke="#0a2f66" stroke-width="1.4"><circle cx="8" cy="8" r="2.2"/><circle cx="8" cy="8" r="5.5" stroke-dasharray="2.2 1.6"/></svg></div><h3>Individuelle Kalibrierung</h3><p>Akkreditiertes Kalibrierlabor für kundenspezifische Kalibrierungen nach DAkkS.</p></div>
      <div class="adv"><div class="adv-icon"><svg width="14" height="14" viewBox="0 0 16 16" fill="none" stroke="#0a2f66" stroke-width="1.4"><path d="M8 1.5l5.5 2v4.5c0 3.2-2.4 5.6-5.5 6.5C4.9 13.6 2.5 11.2 2.5 8V3.5z"/></svg></div><h3>Langlebigkeit</h3><p>Robuste Konstruktion für den Dauereinsatz unter härtesten Industriebedingungen.</p></div>
      <div class="adv"><div class="adv-icon"><svg width="14" height="14" viewBox="0 0 16 16" fill="none" stroke="#0a2f66" stroke-width="1.4"><path d="M2 14V6l4 3V6l4 3V3h4v11z"/></svg></div><h3>Breites Anwendungsspektrum</h3><p>Von der Chemie bis zur Lebensmittelindustrie – für jede Branche die richtige Lösung.</p></div>
      <div class="adv"><div class="adv-icon"><svg width="14" height="14" viewBox="0 0 16 16" fill="none" stroke="#0a2f66" stroke-width="1.4"><path d="M8 14S2 10.2 2 6a3 3 0 0 1 6-1 3 3 0 0 1 6 1c0 4.2-6 8-6 8z"/></svg></div><h3>Persönlicher Support</h3><p>Kompetente technische Beratung und schneller Service durch unser Expertenteam.</p></div>
    </div>
  </div>
</section>

<section class="industries">
  <div class="wrap">
    <div class="ind-text">
      <h2>Einsatz in allen Branchen</h2>
      <p>Unsere Messtechnik bewährt sich täglich in anspruchsvollen Industrieumgebungen</p>
    </div>
    <div class="tiles">
      <div class="tile" style="width:120px"><svg width="16" height="16" viewBox="0 0 16 16" fill="none" stroke="#d15c04" stroke-width="1.4"><path d="M5 1.5h6M6 1.5v5L3 14h10l-3-7.5v-5"/></svg>Chemie &amp; Petrochemie</div>
      <div class="tile" style="width:120px"><svg width="16" height="16" viewBox="0 0 16 16" fill="none" stroke="#d15c04" stroke-width="1.4"><path d="M8 1.5S3.5 7 3.5 10a4.5 4.5 0 0 0 9 0C12.5 7 8 1.5 8 1.5z"/></svg>Wasser &amp; Abwasser</div>
      <div class="tile" style="width:100px"><svg width="16" height="16" viewBox="0 0 16 16" fill="none" stroke="#d15c04" stroke-width="1.4"><rect x="2" y="5.5" width="12" height="5" rx="2.5" transform="rotate(-45 8 8)"/><path d="M6 6l4 4"/></svg>Pharma &amp; Biotech</div>
      <div class="tile" style="width:100px"><svg width="16" height="16" viewBox="0 0 16 16" fill="none" stroke="#d15c04" stroke-width="1.4"><path d="M2 14V6l4 3V6l4 3V3h4v11z"/></svg>Maschinenbau</div>
      <div class="tile" style="width:74px"><svg width="16" height="16" viewBox="0 0 16 16" fill="none" stroke="#d15c04" stroke-width="1.4"><path d="M3 14V2.5h6V14M2 14h8M9 6h2.5l1.5 2v4.5"/></svg>Öl &amp; Gas</div>
      <div class="tile" style="width:114px"><svg width="16" height="16" viewBox="0 0 16 16" fill="none" stroke="#d15c04" stroke-width="1.4"><path d="M9 1.5L3.5 9H8l-1 5.5L12.5 7H8z"/></svg>Energie &amp; Kraftwerke</div>
    </div>
  </div>
</section>

<section class="cta">
  <h2>Bereit für präzise Messtechnik?</h2>
  <p>Lassen Sie sich von unseren Experten beraten. Wir finden die optimale Lösung für Ihre Messaufgabe – individuell und zuverlässig.</p>
  <div class="cta-row">
    <span class="btn-orange">Jetzt anfragen <svg width="10" height="10" viewBox="0 0 10 10"><path d="M1 5h8M5.5 1.5L9 5 5.5 8.5" fill="none" stroke="#fff" stroke-width="1.3"/></svg></span>
    <span class="btn-outline"><svg width="11" height="11" viewBox="0 0 16 16" fill="none" stroke="#14213a" stroke-width="1.5"><path d="M3 1.5h3l1.5 3.5-2 1.5a8 8 0 0 0 4 4l1.5-2 3.5 1.5v3c0 .8-.7 1.5-1.5 1.5A12.5 12.5 0 0 1 1.5 3c0-.8.7-1.5 1.5-1.5z"/></svg>+49 (0) 321 654 90</span>
  </div>
  <small>Oder besuchen Sie unseren <b>Online-Shop</b> für sofortige Bestellungen.</small>
</section>

<footer class="footer">
  <div class="wrap">
    <div class="foot-grid">
      <div>
        <div class="brand"><span class="brand-dot"></span>KTV Sensorik</div>
        <p class="foot-about">KTV GmbH &amp; Co. KG – Ihr Partner für präzise Durchflussmessung und Drucksensorik. Made in Germany.</p>
      </div>
      <ul class="foot-col"><h4>Produkte</h4><li>Durchflussmesser</li><li>Drucksensoren</li><li>Ratgeber</li></ul>
      <ul class="foot-col"><h4>Service</h4><li>Kalibrierung</li><li>Technischer Support</li><li>Downloads</li><li>Online-Shop</li></ul>
      <ul class="foot-col"><h4>Kontakt</h4>
        <li><svg width="10" height="12" viewBox="0 0 12 14" fill="none" stroke="#fff" stroke-width="1.2"><path d="M6 13s4.5-4.2 4.5-7.5a4.5 4.5 0 0 0-9 0C1.5 8.8 6 13 6 13z"/><circle cx="6" cy="5.5" r="1.5"/></svg><span>KTV GmbH &amp; Co. KG<br>Industriestraße 1<br>12345 Musterstadt</span></li>
        <li><svg width="10" height="10" viewBox="0 0 16 16" fill="none" stroke="#fff" stroke-width="1.5"><path d="M3 1.5h3l1.5 3.5-2 1.5a8 8 0 0 0 4 4l1.5-2 3.5 1.5v3c0 .8-.7 1.5-1.5 1.5A12.5 12.5 0 0 1 1.5 3c0-.8.7-1.5 1.5-1.5z"/></svg>+49 (0) 321 654 90</li>
        <li><svg width="11" height="10" viewBox="0 0 16 12" fill="none" stroke="#fff" stroke-width="1.3"><rect x="1" y="1" width="14" height="10" rx="1"/><path d="M1 2l7 5 7-5"/></svg>info@ktv-sensorik.de</li>
      </ul>
    </div>
    <div class="foot-bottom">
      <span>© 2024 KTV GmbH &amp; Co. KG. Alle Rechte vorbehalten.</span>
      <nav><span>Impressum</span><span>Datenschutz</span><span>AGB</span></nav>
    </div>
  </div>
</footer>

</body>
</html>
```